ORLUq Business card. A.I. company developing trading strategies.

My name is tommaso fabbri and I'm CEO and co-founder of ORLUQ Research, an AI company focusing on generating Ai-driven trading strategies.
This is our website: https://orluq-research.example/
Values of our company: tech & R&D driven (we're all very mathy/stats/data driven), sophisticated (we only look for sophisticated, high knowledge investors), reserved (we don't go around telling anyone what we do).
Our main product: KobraFNX. A trading strategy that delivered 70% in 2022 and 20% in 2023 so far.
Our main potential clients: HNW individuals, hedge funds, asset managers, tech entrepreneur.
Hedge funds, asset managers, High Net Worth individuals, Pension funds
The basic: name, job title, company name, address, mail, phone number

```html
<!DOCTYPE html>
<html lang="en">
<head>
<meta charset="UTF-8">
<title>ORLUq Research – Business Card</title>
<link href="https://fonts.googleapis.com/css2?family=Arimo:wght@400;700&display=swap" rel="stylesheet">
<style>
  :root {
    --backdrop: #e6e6e6;
    --card: #2f2f30;
    --card-deep: #2a2a2b;
    --ink-light: #f2f2f2;
    --ink-muted: #d9d9d9;
    --accent: #c4173c;
    --rule: #8a8a8a;
    --emboss: #4a4a4c;
  }
  * { margin: 0; padding: 0; box-sizing: border-box; }
  html, body {
    width: 1200px; height: 802px; overflow: hidden;
    background: var(--backdrop);
    font-family: "Arimo", Arial, sans-serif;
  }
  .canvas {
    position: relative; width: 1200px; height: 802px;
    display: flex; align-items: center; justify-content: center; gap: 60px;
  }
  .card {
    width: 520px; height: 297px;
    background: var(--card);
    position: relative;
    box-shadow: 0 2px 6px rgba(0,0,0,0.18);
  }
  /* Front */
  .card-front { display: flex; align-items: center; padding: 0 34px; }
  .brand {
    width: 210px; display: flex; align-items: center; gap: 10px;
  }
  .brand-name {
    color: var(--ink-light); font-weight: 400; font-size: 26px;
    letter-spacing: 0.06em;
  }
  .brand-dot { width: 8px; height: 8px; border-radius: 50%; background: var(--accent); }
  .divider { width: 1px; height: 150px; background: var(--rule); margin: 0 24px 0 6px; }
  .details { color: var(--ink-muted); font-size: 14px; line-height: 1.3; }
  .person-name {
    color: var(--accent); font-weight: 700; font-size: 19px;
    text-transform: uppercase; letter-spacing: 0.01em;
  }
  .person-role { margin-bottom: 12px; }
  .address { margin-bottom: 12px; }
  .contact-list { list-style: none; }
  .contact-list li { display: flex; align-items: center; gap: 8px; }
  .contact-list svg { width: 11px; height: 11px; fill: var(--accent); flex: none; }
  /* Back */
  .card-back {
    background: var(--card-deep);
    display: flex; align-items: center; justify-content: center;
  }
  .back-brand {
    display: flex; align-items: center; gap: 14px;
  }
  .back-name {
    color: var(--emboss); font-weight: 400; font-size: 44px; letter-spacing: 0.06em;
  }
  .back-dot { width: 10px; height: 10px; border-radius: 50%; background: var(--emboss); }
</style>
</head>
<body>
<main class="canvas">
  <section class="card card-front" aria-label="Business card front">
    <div class="brand">
      <span class="brand-name">ORLUq Research</span>
      <span class="brand-dot"></span>
    </div>
    <div class="divider"></div>
    <div class="details">
      <p class="person-name">Tommaso Fabbri</p>
      <p class="person-role">CEO</p>
      <p class="address">48 rue<br>Vernier 75017 Paris</p>
      <ul class="contact-list">
        <li>
          <svg viewBox="0 0 24 24" aria-hidden="true"><path d="M6.6 10.8a15.1 15.1 0 0 0 6.6 6.6l2.2-2.2a1 1 0 0 1 1-.25 11.4 11.4 0 0 0 3.6.57 1 1 0 0 1 1 1V20a1 1 0 0 1-1 1A17 17 0 0 1 3 4a1 1 0 0 1 1-1h3.5a1 1 0 0 1 1 1c0 1.25.2 2.45.57 3.6a1 1 0 0 1-.25 1z"/></svg>
          800555012
        </li>
        <li>
          <svg viewBox="0 0 24 24" aria-hidden="true"><path d="M2 5h20v14H2z M2 5l10 8 10-8" fill="var(--accent)"/><path d="M3 6l9 7 9-7" stroke="var(--card)" stroke-width="2" fill="none"/></svg>
          info@orluq-research.example
        </li>
        <li>
          <svg viewBox="0 0 24 24" aria-hidden="true"><circle cx="12" cy="12" r="10"/><path d="M2 12h20M12 2c3 3 3 17 0 20M12 2c-3 3-3 17 0 20" stroke="var(--card)" stroke-width="1.5" fill="none"/></svg>
          www.orluq-research.example
        </li>
      </ul>
    </div>
  </section>

  <section class="card card-back" aria-label="Business card back">
    <div class="back-brand">
      <span class="back-name">ORLUq Research</span>
      <span class="back-dot"></span>
    </div>
  </section>
</main>
</body>
</html>
```